Corrindale Planners, LLC Stationary

Corrindale Planners, LLC is a new financial planning and consulting company. We are looking for designs on business cards, letterhead, envelopes, and anything else that would be useful. Our preference for business card design is two sided. We are looking for a professional and clean look with incorporating the logo and patriotic feel. Thank you to all who participate and good luck!

```html
<!DOCTYPE html>
<html lang="en">
<head>
<meta charset="utf-8">
<title>Corrindale Planners, LLC — Stationery</title>
<link href="https://fonts.googleapis.com/css2?family=Montserrat:wght@500;700&family=Open+Sans:wght@400;600&display=swap" rel="stylesheet">
<style>
  :root {
    --navy: #1f3a63;
    --red: #c7262f;
    --ink: #3b3f46;
    --muted: #7a808a;
    --paper: #ffffff;
    --stage: #eceef0;
    --logo-font: "Montserrat", Arial, sans-serif;
    --body-font: "Open Sans", Arial, sans-serif;
  }
  * { box-sizing: border-box; margin: 0; padding: 0; }
  html, body { width: 1200px; height: 794px; overflow: hidden; background: var(--stage); }
  .canvas { position: relative; width: 1200px; height: 794px; }

  .brand { display: flex; align-items: center; gap: 7px; font-family: var(--logo-font); font-weight: 700; color: var(--navy); letter-spacing: .02em; }
  .brand-mark { width: 10px; height: 10px; background: var(--red); flex: none; }

  /* Letterhead */
  .letterhead {
    position: absolute; left: 120px; top: 93px; width: 430px; height: 608px;
    background: var(--paper); box-shadow: 0 6px 18px rgba(0,0,0,.12);
    padding: 40px 44px 0; font-family: var(--body-font); color: var(--ink);
  }
  .letterhead .brand { font-size: 13px; }
  .letter { margin-top: 34px; font-size: 7.6px; line-height: 1.6; }
  .letter p { margin-bottom: 10px; }
  .letter .address { margin-bottom: 12px; }
  .signature {
    width: 88px; height: 26px; margin: 6px 0 2px;
    background: linear-gradient(90deg, #d9dce1, #eef0f2);
    border-radius: 3px;
  }
  .letter .role { font-size: 7.6px; }
  .letter-rule { position: absolute; left: 0; right: 0; bottom: 48px; height: 3px; background: var(--navy); }
  .letter-rule::after { content: ""; position: absolute; right: 0; top: 0; width: 70px; height: 3px; background: var(--red); }
  .letter-footer {
    position: absolute; left: 0; right: 0; bottom: 26px; text-align: center;
    font-family: var(--logo-font); font-size: 6.4px; color: var(--muted); letter-spacing: .04em;
  }

  /* Business cards */
  .card {
    position: absolute; left: 650px; width: 420px; height: 240px;
    box-shadow: 0 6px 18px rgba(0,0,0,.12);
  }
  .card-front { top: 145px; background: var(--navy); display: flex; align-items: center; padding-left: 44px; }
  .card-front .brand { color: #fff; font-size: 19px; }
  .card-front .brand-mark { width: 14px; height: 14px; }

  .card-back { top: 425px; background: var(--paper); padding: 30px 32px; font-family: var(--body-font); color: var(--ink); }
  .card-back .brand { font-size: 15px; }
  .card-back .brand-mark { width: 12px; height: 12px; }
  .contact { position: absolute; right: 32px; top: 32px; text-align: right; font-family: var(--logo-font); font-size: 8px; line-height: 1.8; color: var(--muted); }
  .person { position: absolute; left: 32px; bottom: 40px; }
  .person-name { font-family: var(--logo-font); font-weight: 700; font-size: 11px; color: var(--navy); letter-spacing: .06em; }
  .person-title { font-size: 8px; color: var(--red); margin-top: 2px; }
  .card-back-rule { position: absolute; left: 0; right: 0; bottom: 0; height: 6px; background: var(--navy); }
  .card-back-rule::after { content: ""; position: absolute; right: 0; top: 0; width: 90px; height: 6px; background: var(--red); }
</style>
</head>
<body>
<main class="canvas">

  <section class="letterhead">
    <div class="brand"><span class="brand-mark"></span>Corrindale Planners, LLC</div>
    <div class="letter">
      <p class="address">November 1, 2014<br>Mr. Ellis Warren<br>1204 Birchwood Lane<br>Lancaster, PA 17601</p>
      <p>Dear Mr. Warren:</p>
      <p>The first paragraph of a typical business letter is used to state the main point of the letter. Begin with a friendly opening, then quickly move into the purpose of your letter. Use a couple of sentences to explain the purpose, but do not go into detail until the next paragraph.</p>
      <p>Beginning with the second paragraph, state the supporting details to justify your purpose. These may take the form of background information, statistics or first-hand accounts. A few short paragraphs within the body of the letter should be enough to support your reasoning.</p>
      <p>Finally, in the closing paragraph, briefly restate your purpose and why it is important. If the purpose of your letter is employment related, consider ending your letter with your contact information. Close by thanking the reader for their time.</p>
      <p>Sincerely,</p>
      <div class="signature" role="img" aria-label="Handwritten signature"></div>
      <div class="role">President</div>
    </div>
    <div class="letter-rule"></div>
    <div class="letter-footer">4410 Market Street, Suite 210, Lancaster, PA 17601 &nbsp;|&nbsp; T: (717) 555-0148 &nbsp;|&nbsp; www.corrindaleplanners.com</div>
  </section>

  <section class="card card-front">
    <div class="brand"><span class="brand-mark"></span>Corrindale Planners, LLC</div>
  </section>

  <section class="card card-back">
    <div class="brand"><span class="brand-mark"></span>Corrindale Planners, LLC</div>
    <div class="contact">4410 Market Street, Suite 210<br>Lancaster, PA 17601<br>T: (717) 555-0148<br>www.corrindaleplanners.com</div>
    <div class="person">
      <div class="person-name">ALDEN MARSH</div>
      <div class="person-title">Senior Advisor</div>
    </div>
    <div class="card-back-rule"></div>
  </section>

</main>
</body>
</html>
```